Brookvale Insurance Services - Insurance Agency Wesbite

I need a website for my insurance agency called Brookvale Insurance Services. I have attached my company logo. You can use the colors from the copy logo to create the website color scheme. I need a Request A Quote section.
Business Address: 7316 Marlowe Ave Unit D, Ashgrove Ca 95999
Business Phone: (555) 555-0193
I would need the following drop downs on the main page:

1st drop down:
Business Insurance
⁃ Commercial Auto
⁃ Employment Practice Liability Insurance
⁃ General Liability Insurance
⁃ Professional Liability Insurance
⁃ Property Insurance
⁃ Workers Compensation Insurance

2nd drop down:
Industries We Serve
- Construction
- Janitorial
- Landscapers
- Trucking
- ParcelWay Independent Service Providers (ISP)
Healthcare Industry
- Community Care Facilities
- Home Health Agencies
- Hospice
- Nursing Homes

3rd drop down:
Risk Management
- Claims Management
- Compliance & Risk Management

4th drop down
Request a quote

5th drop down
About Us

6th drop down
Contact US

Target Market(s)

Potential clients

Industry/Entity Type

Business Insurance

Coding

Coded - Design and coding required

Number of Pages Required

5+ page

Colors
0054AA
0677BA
7BADD7
CADEEF
E8F1F8
00AB8E
00BBA5
67D7C9
C6EFE9
E9F9F6

Requirements
Must have
• Home Business Insurance - Commercial Auto - Employment Practice Liability Insurance - General Liability Insurance - Professional Liability Insurance - Property Insurance - Workers Compensation Insurance Industries We Serve - Construction - Janitorial - Landscapers - Manufacturing Companies - Restaurants - Towing - Trucking Healthcare Industry - Community Care Facilities - Home Health Agencies - Hospice - Nursing Homes - Risk Management - Claims Management - Compliance & Risk Management Request a Quote About Us Contact Us

```html
<!DOCTYPE html>
<html lang="en">
<head>
<meta charset="utf-8">
<title>Brookvale Insurance Services</title>
<link href="https://fonts.googleapis.com/css2?family=Roboto:wght@400;500;700;900&family=Great+Vibes&display=swap" rel="stylesheet">
<style>
:root{
  --green:#1c9a3c;
  --green-dark:#13802e;
  --green-pale:#e9f7ee;
  --navy:#1b2a4a;
  --ink:#222;
  --muted:#666;
  --line:#dcdcdc;
  --footer:#16191f;
  --white:#fff;
}
*{box-sizing:border-box;margin:0;padding:0}
html,body{width:1200px;height:4044px;overflow:hidden}
body{font-family:'Roboto',sans-serif;color:var(--ink);background:var(--white);position:relative}
.abs{position:absolute}
/* header */
.site-header{position:absolute;top:0;left:0;width:1200px;height:60px;background:var(--white);display:flex;align-items:center;padding:0 120px;z-index:2}
.brand{font-weight:900;color:var(--green);font-size:20px;letter-spacing:.5px;display:flex;align-items:center;gap:8px;line-height:1}
.brand small{display:block;font-size:8px;font-weight:900;letter-spacing:2px}
.brand-dot{width:14px;height:14px;background:var(--green)}
.main-nav{display:flex;gap:26px;margin-left:80px;font-size:12px;font-weight:500}
.main-nav a{color:var(--ink);text-decoration:none}
.main-nav a.active{color:var(--green)}
.btn{display:inline-flex;align-items:center;justify-content:center;background:var(--green);color:#fff;font-weight:500;text-decoration:none;border:0}
.header-cta{margin-left:auto;height:40px;width:126px;font-size:14px}
/* hero */
.hero{top:60px;left:0;width:1200px;height:620px;background:linear-gradient(90deg,#2e3a22 0%,#4f5c3a 35%,#8c8f78 65%,#b9b3a3 100%)}
.hero-copy{left:120px;top:40px;width:440px;color:#fff}
.hero-welcome{font-family:'Great Vibes',cursive;color:#4cd16c;font-size:40px}
.hero-title{font-size:38px;font-weight:900;line-height:1.15;margin-top:4px}
.hero-text{font-size:13px;line-height:1.6;margin-top:14px;opacity:.95}
.hero-btn{margin-top:150px;width:130px;height:52px;font-size:15px}
/* section titles */
.section-title{width:1200px;left:0;text-align:center;font-size:40px;font-weight:900}
.section-title .g{color:var(--green)}
.section-title .d{color:var(--navy)}
/* business cards */
.biz-grid{top:830px;left:116px;display:flex;gap:14px}
.biz-card{width:150px;height:106px;background:#fff;box-shadow:0 3px 12px rgba(0,0,0,.12);padding:18px 14px;font-size:11px;line-height:1.35}
.biz-card svg{display:block;margin-bottom:10px}
.biz-btn{top:968px;left:460px;width:280px;height:52px;font-size:15px}
/* risk */
.risk{top:1080px;left:0;width:1200px;height:520px;background:linear-gradient(180deg,#eef8f1,#f7fcf8)}
.photo{background:linear-gradient(135deg,#8a7b6e,#c9b9a6 55%,#5d5a5a)}
.risk-main{left:112px;top:72px;width:480px;height:400px}
.risk-card{left:600px;width:488px;height:194px;display:flex}
.risk-card .photo{width:110px;height:100%}
.risk-card .panel{flex:1;background:var(--green);color:#fff;padding:18px 22px}
.risk-card h3{font-size:22px;font-weight:700;line-height:1.15}
.risk-card p{font-size:12px;line-height:1.55;margin-top:8px}
/* industries */
.tab{top:1688px;height:84px;width:340px;display:flex;align-items:center;justify-content:center;font-weight:700;font-size:17px}
.tab-on{left:240px;background:var(--green);color:#fff}
.tab-off{left:620px;background:var(--green-pale);color:var(--green)}
.hub{left:448px;top:1848px;width:304px;height:304px;border-radius:50%;background:var(--green);color:#fff;display:flex;flex-direction:column;align-items:center;justify-content:center;font-weight:900}
.hub b{font-size:36px;letter-spacing:1px}
.hub span{font-size:13px;letter-spacing:3px;margin-top:4px}
.industry{width:180px;text-align:center;font-size:14px;font-weight:700;color:var(--ink)}
.industry .ic{width:60px;height:60px;border-radius:50%;border:2px solid var(--green);margin:0 auto 10px;display:flex;align-items:center;justify-content:center}
/* quote */
.map{top:2428px;left:0;width:1200px;height:572px;background:linear-gradient(135deg,#e7e9ec,#dfe3e6 50%,#eceef0)}
.quote-card{left:120px;top:2488px;width:640px;height:492px;background:#fff;box-shadow:0 4px 18px rgba(0,0,0,.15);padding:30px 28px}
.quote-card h2{font-size:40px;font-weight:900}
.quote-card h2 .g{color:var(--green)}.quote-card h2 .d{color:var(--navy)}
.field{border:1px solid var(--line);height:44px;font-size:12px;color:#888;padding:14px 16px;margin-top:14px}
.row{display:flex;gap:14px}.row .field{flex:1}
.field.msg{height:94px}
.submit{margin-top:20px;width:132px;height:52px;font-size:14px}
/* events */
.event{top:3132px;width:290px;height:312px;background:var(--green);color:#fff}
.event .photo{height:150px;margin:8px 8px 0}
.event .body{padding:12px 16px}
.event h4{font-size:17px;font-weight:700;line-height:1.25}
.event .date{font-size:11px;margin-top:6px}
.event p{font-size:12px;font-weight:700;margin-top:8px;line-height:1.35}
.arrow{top:3264px;width:44px;height:44px;border-radius:50%;border:1px solid #999;display:flex;align-items:center;justify-content:center}
.partners{top:3612px;left:200px;width:800px;display:flex;justify-content:space-between}
.partners span{height:26px;background:#cfd2d6;border-radius:3px}
/* footer */
.site-footer{top:3712px;left:0;width:1200px;height:332px;background:var(--footer);color:#cfd2d6}
.site-footer .brand{color:#fff}
.f-col{font-size:13px;line-height:2.1}
.f-col h5{color:var(--green);font-size:15px;font-weight:700;margin-bottom:6px}
.f-line{display:flex;align-items:center;gap:10px;white-space:nowrap}
.f-ico{width:18px;height:18px;border-radius:50%;background:#fff;flex:none}
.copy{left:0;width:1200px;top:308px;text-align:center;font-size:11px;color:#9aa0a8}
</style>
</head>
<body>

<header class="site-header">
  <div class="brand"><span class="brand-dot"></span><div>BROOKVALE<small>INSURANCE SERVICES</small></div></div>
  <nav class="main-nav">
    <a class="active" href="#">Home</a><a href="#">About Us</a><a href="#">Business Insurance ▾</a><a href="#">Industries We Serve ▾</a><a href="#">Risk Management ▾</a>
  </nav>
  <a class="btn header-cta" href="#">Contact us</a>
</header>

<section class="abs hero" role="img" aria-label="Photo of a smiling older couple embracing outdoors">
  <div class="abs hero-copy">
    <div class="hero-welcome">Welcome to</div>
    <h1 class="hero-title">BROOKVALE<br>INSURANCE SERVICES</h1>
    <p class="hero-text">We help local businesses protect what they have built with clear advice, fair pricing and coverage that fits. Our team compares trusted carriers so you get the right policy, fast support and one partner for every claim and renewal.</p>
    <a class="btn hero-btn" href="#">Get started</a>
  </div>
</section>

<h2 class="abs section-title" style="top:730px"><span class="g">BUSINESS</span> <span class="d">INSURANCE</span></h2>
<div class="abs biz-grid">
  <div class="biz-card"><svg width="22" height="16" viewBox="0 0 22 16"><rect x="1" y="3" width="13" height="9" fill="none" stroke="#1c9a3c" stroke-width="2"/><path d="M14 6h4l3 3v3h-7z" fill="none" stroke="#1c9a3c" stroke-width="2"/><circle cx="5" cy="14" r="1.6" fill="#1c9a3c"/><circle cx="17" cy="14" r="1.6" fill="#1c9a3c"/></svg>Commercial Auto</div>
  <div class="biz-card"><svg width="18" height="18" viewBox="0 0 18 18"><circle cx="9" cy="6" r="4" fill="#1c9a3c"/><path d="M2 17c0-4 3-6 7-6s7 2 7 6z" fill="#1c9a3c"/></svg>Employment Practice Liability Insurance</div>
  <div class="biz-card"><svg width="18" height="18" viewBox="0 0 18 18"><path d="M9 1l7 3v5c0 4-3 7-7 8-4-1-7-4-7-8V4z" fill="#1c9a3c"/></svg>General Liability Insurance</div>
  <div class="biz-card"><svg width="18" height="18" viewBox="0 0 18 18"><rect x="1" y="5" width="16" height="11" fill="#1c9a3c"/><rect x="6" y="2" width="6" height="4" fill="none" stroke="#1c9a3c" stroke-width="2"/></svg>Professional Liability Insurance</div>
  <div class="biz-card"><svg width="18" height="18" viewBox="0 0 18 18"><path d="M1 9l8-7 8 7h-2v8H3V9z" fill="#1c9a3c"/></svg>Property Insurance</div>
  <div class="biz-card"><svg width="18" height="18" viewBox="0 0 18 18"><path d="M3 9a6 6 0 0 1 12 0z" fill="#1c9a3c"/><rect x="1" y="9" width="16" height="3" fill="#1c9a3c"/></svg>Workers Compensation Insurance</div>
</div>
<a class="abs btn biz-btn" href="#">View All Business Insurance</a>

<section class="abs risk" role="img" aria-label="Light green background with a faint line pattern">
  <div class="abs photo risk-main" role="img" aria-label="Photo of an advisor meeting with a couple in an office"></div>
  <div class="abs risk-card" style="top:72px">
    <div class="photo" role="img" aria-label="Photo of a man reviewing documents at a desk"></div>
    <div class="panel"><h3>Claims Management</h3><p>Our approach to claims management keeps every file moving. We guide you through each step, report quickly to carriers and keep you informed until the claim is fairly settled and closed.</p></div>
  </div>
  <div class="abs risk-card" style="top:278px">
    <div class="photo" role="img" aria-label="Photo of a woman working on a laptop"></div>
    <div class="panel"><h3>Compliance &amp; Risk<br>Management</h3><p>Effective risk management lowers losses and costs. We review your operations, spot gaps in safety and contracts, and build a simple plan to stay compliant.</p></div>
  </div>
</section>

<div class="abs tab tab-on">INDUSTRIES WE SERVE</div>
<div class="abs tab tab-off">HEALTHCARE INDUSTRY</div>
<div class="abs hub"><b>BROOKVALE</b><span>INSURANCE SERVICES</span></div>

<div class="abs industry" style="left:150px;top:1830px"><div class="ic"><svg width="28" height="28" viewBox="0 0 28 28"><path d="M4 18a10 10 0 0 1 20 0z" fill="#1c9a3c"/><rect x="2" y="18" width="24" height="4" fill="#1c9a3c"/></svg></div>CONSTRUCTION</div>
<div class="abs industry" style="left:190px;top:2024px"><div class="ic"><svg width="26" height="26" viewBox="0 0 26 26"><path d="M13 2l9 4v7c0 6-4 10-9 11-5-1-9-5-9-11V6z" fill="#1c9a3c"/><path d="M9 13l3 3 5-6" stroke="#fff" stroke-width="2.4" fill="none"/></svg></div>JANITORIAL</div>
<div class="abs industry" style="left:310px;top:2168px"><div class="ic"><svg width="26" height="26" viewBox="0 0 26 26"><path d="M13 3l8 14H5z" fill="#1c9a3c"/><rect x="12" y="17" width="2" height="6" fill="#1c9a3c"/></svg></div>LANDSCAPERS</div>
<div class="abs industry" style="left:510px;top:2224px"><div class="ic"><svg width="26" height="26" viewBox="0 0 26 26"><path d="M3 22V12l6 4v-4l6 4V6h6v16z" fill="#1c9a3c"/></svg></div>MANUFACTURING<br>COMPANIES</div>
<div class="abs industry" style="left:690px;top:2168px"><div class="ic"><svg width="26" height="26" viewBox="0 0 26 26"><path d="M8 3v8M6 3v6a2 2 0 0 0 4 0V3M8 11v12M18 3c-3 2-3 8 0 9v11" stroke="#1c9a3c" stroke-width="2.2" fill="none"/></svg></div>RESTAURANTS</div>
<div class="abs industry" style="left:830px;top:2024px"><div class="ic"><svg width="28" height="24" viewBox="0 0 28 24"><rect x="2" y="8" width="14" height="9" fill="#1c9a3c"/><path d="M16 11h5l4 4v2h-9z" fill="#1c9a3c"/><circle cx="7" cy="19" r="2.5" fill="#1c9a3c"/><circle cx="21" cy="19" r="2.5" fill="#1c9a3c"/></svg></div>TOWING</div>
<div class="abs industry" style="left:830px;top:1840px"><div class="ic"><svg width="28" height="24" viewBox="0 0 28 24"><rect x="1" y="5" width="17" height="12" fill="#1c9a3c"/><path d="M18 9h5l4 4v4h-9z" fill="#1c9a3c"/><circle cx="6" cy="19" r="2.5" fill="#1c9a3c"/><circle cx="22" cy="19" r="2.5" fill="#1c9a3c"/></svg></div>TRUCKING</div>

<section class="abs map" role="img" aria-label="Street map showing the office location"></section>
<svg class="abs" style="left:892px;top:2760px" width="24" height="34" viewBox="0 0 24 34"><path d="M12 0a12 12 0 0 1 12 12c0 9-12 22-12 22S0 21 0 12A12 12 0 0 1 12 0z" fill="#e53935"/><circle cx="12" cy="12" r="4.5" fill="#fff"/></svg>
<form class="abs quote-card">
  <h2><span class="g">REQUEST</span> <span class="d">A QUOTE</span></h2>
  <div class="row"><div class="field">First Name</div><div class="field">Last Name</div></div>
  <div class="field">Email</div>
  <div class="field">Address</div>
  <div class="field msg">Message</div>
  <button class="btn submit" type="button">Submit</button>
</form>

<h2 class="abs section-title" style="top:3052px"><span class="g">LATEST</span> <span class="d">EVENTS</span></h2>
<div class="abs arrow" style="left:38px"><svg width="10" height="14" viewBox="0 0 10 14"><path d="M8 1L2 7l6 6" stroke="#555" stroke-width="2" fill="none"/></svg></div>
<div class="abs arrow" style="left:1118px"><svg width="10" height="14" viewBox="0 0 10 14"><path d="M2 1l6 6-6 6" stroke="#555" stroke-width="2" fill="none"/></svg></div>
<article class="abs event" style="left:160px"><div class="photo" role="img" aria-label="Photo of a team meeting around a table"></div><div class="body"><h4>Lorem Ipsum is simply dummy text of the printing and</h4><div class="date">April 1st — April 03, 2022</div><p>Lorem Ipsum is simply dummy text of the printing and typesetting industry.</p></div></article>
<article class="abs event" style="left:474px"><div class="photo" role="img" aria-label="Photo of colleagues discussing at a laptop"></div><div class="body"><h4>Lorem Ipsum is simply dummy text of the printing and</h4><div class="date">April 1st — April 03, 2022</div><p>Lorem Ipsum is simply dummy text of the printing and typesetting industry.</p></div></article>
<article class="abs event" style="left:788px"><div class="photo" role="img" aria-label="Photo of an advisor shaking hands with a client"></div><div class="body"><h4>Lorem Ipsum is simply dummy text of the printing and</h4><div class="date">April 1st — April 03, 2022</div><p>Lorem Ipsum is simply dummy text of the printing and typesetting industry.</p></div></article>

<div class="abs partners"><span style="width:90px"></span><span style="width:120px"></span><span style="width:120px"></span><span style="width:130px"></span><span style="width:150px"></span></div>

<footer class="abs site-footer">
  <div class="abs" style="left:120px;top:56px;width:190px">
    <div class="brand"><span class="brand-dot"></span><div>BROOKVALE<small>INSURANCE SERVICES</small></div></div>
    <p style="font-size:11px;line-height:1.6;margin-top:16px">Local coverage for growing businesses, backed by trusted carriers and a team that answers when you call.</p>
  </div>
  <div class="abs f-col" style="left:368px;top:44px"><h5>MENU</h5>Home<br>About Us<br>Business Insurance<br>Industries We Serve<br>Risk Management</div>
  <div class="abs f-col" style="left:568px;top:44px"><h5>CONTACT US</h5>
    <div class="f-line"><span class="f-ico"></span>(555) 555-0193</div>
    <div class="f-line"><span class="f-ico"></span>7316 Marlowe Ave Unit D, Ashgrove Ca 95999</div>
    <div class="f-line"><span class="f-ico"></span>info@brookvale-insurance.example</div>
  </div>
  <div class="abs f-col" style="left:928px;top:44px"><h5>FOLLOW US</h5>
    <div class="f-line"><span class="f-ico"></span>Chatterbook</div>
    <div class="f-line"><span class="f-ico"></span>ClipStream</div>
    <div class="f-line"><span class="f-ico"></span>Snapgram</div>
    <div class="f-line"><span class="f-ico"></span>Chirper</div>
  </div>
  <div class="abs copy">Copyright © 2015-2024 Brookvale Insurance Services LLC. All rights reserved.</div>
</footer>

</body>
</html>
```